Wedding Day Custom Wine Label - Tasmanian (Tamar Valley) wine

I am looking for a custom design that will be put on a wine label to commemorate a very good friend's wedding day.

We will need to be able to take the design and print it on to sticker labels that we can put on to wine bottles.

The bride and groom have asked for a simplistic label design (see example image attached). We need two labels. One for "Pinot Noir" wine and the other for "Chardonnay" wine. We would like the label to say:

The Hartwell's
Pinot Noir
2023
Tamar Valley

and for for the other wine variety:

The Hartwell's
Chardonnay
2023
Tamar Valley

smaller text below to say:

13.5% ALC/VOL 750ML
MEGAN & LIAM - 31.10.2024

I am happy to consider other variations - the bride & groom would prefer something minimalistic. Elegant and classy.

Target Market(s)

the bride & groom

Requirements
Must have
• Wedding date (31.10.2024). Wine type (Pinot Noir or Chardonnay).
Should not have
• images not essential

```html
<!DOCTYPE html>
<html lang="en">
<head>
<meta charset="utf-8">
<title>The Hartwell's – Wedding Wine Labels</title>
<link rel="stylesheet" href="https://fonts.googleapis.com/css2?family=Bodoni+Moda:opsz,wght@6..96,500&family=Italiana&family=Archivo+Black&family=Great+Vibes&display=swap">
<style>
  :root {
    --ink: #000000;
    --paper: #ffffff;
  }
  html, body {
    margin: 0;
    padding: 0;
    width: 776px;
    height: 1200px;
    overflow: hidden;
    background: var(--paper);
  }
  .label-sheet { display: block; width: 776px; height: 1200px; }
  .frame-outer { fill: none; stroke: var(--ink); stroke-width: 10; }
  .frame-inner { fill: none; stroke: var(--ink); stroke-width: 2; }
  .rule { stroke: var(--ink); stroke-width: 1.4; }
  .band { fill: var(--ink); }
  .script-article {
    font-family: "Great Vibes", cursive;
    font-size: 40px;
    fill: var(--ink);
    stroke: var(--paper);
    stroke-width: 3;
    paint-order: stroke;
  }
  .family-name {
    font-family: "Bodoni Moda", serif;
    font-weight: 500;
    font-size: 64px;
    fill: var(--ink);
  }
  .variety {
    font-family: "Italiana", serif;
    font-size: 46px;
    fill: var(--ink);
  }
  .vintage {
    font-family: "Archivo Black", sans-serif;
    font-size: 27px;
    letter-spacing: 3px;
    fill: var(--ink);
  }
  .region {
    font-family: "Archivo Black", sans-serif;
    font-size: 14px;
    letter-spacing: 2.2px;
    fill: var(--ink);
  }
  .details {
    font-family: "Archivo Black", sans-serif;
    font-size: 14px;
    letter-spacing: 1.4px;
    fill: var(--paper);
  }
</style>
</head>
<body>
<svg class="label-sheet" viewBox="0 0 776 1200" xmlns="http://www.w3.org/2000/svg">
  <defs>
    <g id="label-frame">
      <rect class="frame-outer" x="188" y="101" width="398" height="393" rx="22"/>
      <rect class="frame-inner" x="206" y="119" width="362" height="357" rx="10"/>
      <rect class="band" x="207" y="158" width="360" height="22"/>
      <line class="rule" x1="206" y1="266" x2="206" y2="410"/>
      <line class="rule" x1="568" y1="266" x2="568" y2="410"/>
      <line class="rule" x1="233" y1="277" x2="533" y2="277"/>
      <line class="rule" x1="240" y1="339" x2="510" y2="339"/>
      <path class="band" d="M207 410 H567 V465 Q567 475 557 475 H217 Q207 475 207 465 Z"/>
    </g>
  </defs>

  <g class="label label--pinot">
    <use href="#label-frame"/>
    <text class="script-article" x="380" y="192" text-anchor="middle">the</text>
    <text class="family-name" x="206" y="252" textLength="362" lengthAdjust="spacingAndGlyphs">HARTWELL'S</text>
    <text class="variety" x="386" y="327" text-anchor="middle" textLength="316" lengthAdjust="spacingAndGlyphs">PINOT NOIR</text>
    <text class="vintage" x="386" y="370" text-anchor="middle">2023</text>
    <text class="region" x="386" y="394" text-anchor="middle">TAMAR VALLEY</text>
    <text class="details" x="387" y="440" text-anchor="middle">13.5% ALC/VOL 750ML</text>
    <text class="details" x="387" y="461" text-anchor="middle">MEGAN &amp; LIAM · 31·10·2024</text>
  </g>

  <g class="label label--chardonnay" transform="translate(0 498)">
    <use href="#label-frame"/>
    <text class="script-article" x="380" y="192" text-anchor="middle">the</text>
    <text class="family-name" x="206" y="252" textLength="362" lengthAdjust="spacingAndGlyphs">HARTWELL'S</text>
    <text class="variety" x="386" y="326" text-anchor="middle" textLength="330" lengthAdjust="spacingAndGlyphs">CHARDONNAY</text>
    <text class="vintage" x="386" y="370" text-anchor="middle">2023</text>
    <text class="region" x="386" y="394" text-anchor="middle">TAMAR VALLEY</text>
    <text class="details" x="387" y="440" text-anchor="middle">13.5% ALC/VOL 750ML</text>
    <text class="details" x="387" y="461" text-anchor="middle">MEGAN &amp; LIAM · 31·10·2024</text>
  </g>
</svg>
</body>
</html>
```